Brochure Design Project

Create a design for parent and family education program (using attached text) that can serve as a template for other brochures

Industry/Entity Type

Education

Requirements
Must have
• leave space for one logo (same logo as on attached)

```html
<!DOCTYPE html>
<html lang="en">
<head>
<meta charset="utf-8">
<title>Oh Baby! – Family Education Classes</title>
<link href="https://fonts.googleapis.com/css2?family=Gilda+Display&family=Arimo:wght@400;700&display=swap" rel="stylesheet">
<style>
  :root {
    --teal: #4f9ea8;
    --grey-text: #8c8c8c;
    --body-text: #1f1f1f;
    --page: #ffffff;
    --backdrop: #ffffff;
    --gutter-shade: #d9d9d9;
    --logo-blue: #1d4f8c;
  }
  * { box-sizing: border-box; margin: 0; padding: 0; }
  html, body { width: 1200px; height: 927px; overflow: hidden; background: var(--backdrop); }
  body { font-family: "Arimo", Arial, sans-serif; color: var(--body-text); }

  .spread {
    position: absolute; left: 48px; top: 36px;
    width: 1098px; height: 848px;
    display: flex;
    box-shadow: 0 2px 10px rgba(0,0,0,0.18);
  }
  .page { position: relative; width: 549px; height: 848px; background: var(--page); overflow: hidden; }
  .page--left { background: linear-gradient(to right, #ffffff 80%, #f1f1f1 100%); }
  .page--right { background: linear-gradient(to right, var(--gutter-shade) 0%, #f4f4f4 12%, #ffffff 30%); }

  .title {
    position: absolute; left: 44px; top: 42px; z-index: 2;
    font-family: "Gilda Display", "Times New Roman", serif;
    font-size: 97px; line-height: 1; font-weight: 400;
    color: var(--teal); letter-spacing: -1px;
  }
  .intro {
    position: absolute; left: 50px; top: 140px; width: 300px; z-index: 2;
    font-size: 17.5px; line-height: 23px; color: var(--grey-text);
  }

  .column { position: absolute; width: 208px; z-index: 2; }
  .col-l1 { left: 50px; top: 218px; }
  .col-l2 { left: 288px; top: 218px; }
  .col-r1 { left: 48px; top: 50px; }
  .col-r2 { left: 288px; top: 50px; }

  .class-title {
    font-size: 15.5px; line-height: 18.5px; font-weight: 700;
    color: var(--teal);
  }
  .class-text { font-size: 12.5px; line-height: 14.1px; margin-bottom: 12px; }
  .options { list-style: none; }
  .options li { color: var(--teal); font-weight: 700; }
  .options li::before { content: "• "; }

  .photo { position: absolute; z-index: 1; }
  .photo--baby {
    left: 97px; top: 610px; width: 452px; height: 238px;
    background: radial-gradient(ellipse at 45% 50%, #f1ddd0 0%, #f6eae2 40%, #ffffff 75%);
  }
  .photo--family {
    left: 75px; top: 566px; width: 430px; height: 282px;
    background: linear-gradient(to bottom, #f7f4f1 0%, #efe5dc 45%, #e8e8ec 100%);
  }

  .brand {
    position: absolute; left: 286px; top: 497px; z-index: 2;
    display: flex; align-items: center; gap: 8px;
  }
  .brand-mark { width: 42px; height: 42px; border: 3px solid var(--logo-blue); }
  .brand-name {
    font-family: "Gilda Display", "Times New Roman", serif;
    font-size: 23px; line-height: 24px; color: var(--logo-blue);
  }
</style>
</head>
<body>
  <div class="spread">
    <section class="page page--left">
      <h1 class="title">Oh Baby!</h1>
      <p class="intro">Harbor Grace offers comprehensive health advice to keep your little ones well — from birth and beyond.</p>

      <div class="column col-l1">
        <h2 class="class-title">Childbirth Preparation<br>‘All About Birth’</h2>
        <div class="class-text">During All About Birth, we will help you prepare for what you might expect during your labor, birth and postpartum. Our class combines interaction with our knowledgeable childbirth educators and online resources for your continued learning. Options for participating include:
          <ul class="options">
            <li>Two evening classes</li>
            <li>One half day Saturday class</li>
            <li>Online course</li>
          </ul>
          (note this course is taken at your convenience and does not include class time with our childbirth educators)</div>

        <h2 class="class-title">Breastfeeding</h2>
        <div class="class-text">Get the basics you need for successful breastfeeding. This class includes techniques and tips to get you off to a good start and ideas to help fit breastfeeding into your lifestyle. Birth partners and other family members are encouraged to attend.</div>
      </div>

      <div class="column col-l2">
        <h2 class="class-title">Breastfeeding Support: Mom2Mom</h2>
        <div class="class-text">Join other mothers and their babies to share experiences, get encouragement, and learn ideas from experienced lactation consultants.</div>

        <h2 class="class-title">Newborn Care</h2>
        <div class="class-text">Get the latest information on baby care basics, safety, early brain development and common new parent concerns in this interactive class.</div>
      </div>

      <div class="photo photo--baby" role="img" aria-label="Photo of a baby lying on its tummy reaching forward"></div>
    </section>

    <section class="page page--right">
      <div class="column col-r1">
        <h2 class="class-title">CPR-Infant-Child</h2>
        <div class="class-text">From birth to age 8, learn the basic life support (BLS) skills according to National Cardiac Council (NCC) guidelines.</div>

        <h2 class="class-title">Infant Child First Aid: What to Do in an Emergency</h2>
        <div class="class-text">This course will discuss prevention and how to avoid medical emergencies included will be hands-on first aid stations with real life scenarios for practice so that you will know what to do in an emergency.</div>

        <h2 class="class-title">Sure Sitter</h2>
        <div class="class-text">Sure Sitter Basic is a medically accurate, hands-on, class that teaches boys and girls ages 11–13 how to handle emergencies when caring for children. This class teaches safe and nurturing child care techniques, behavior management skills and appropriate response to medical emergencies.</div>

        <h2 class="class-title">Child Passenger Safety</h2>
        <div class="class-text">Motor vehicle crashes are the leading cause of injury-related death among children ages 4 and under. Car seat checks by a Certified Child Passenger Safety Technician are available at all of our metro locations. Call to schedule an appointment.</div>
      </div>

      <div class="column col-r2">
        <h2 class="class-title">Siblings for Life</h2>
        <div class="class-text">This fun and interactive class emphasizes the role of the older sibling and helps prepare them to welcome their new brother or sister. For children ages 3-9.</div>

        <h2 class="class-title">Baby Sing and Sign</h2>
        <div class="class-text">Learn to communicate with your baby through song and signs in four simple sessions. The class is recommended for babies and toddlers 6 to 18 months.</div>

        <h2 class="class-title">Water Works! Aqua Mom Fitness</h2>
        <div class="class-text">Expecting moms and new moms: Water Works! Get a low-impact, lowintensity aqua workout to increase your energy and reduce fatigue. (Prenatal doctor’s release required).</div>

        <h2 class="class-title">Parent &amp; Tot Aqua</h2>
        <div class="class-text">Explore the water as a safe and fun environment for you and your child. In-water participation is required of a guardian or parent. Water activities progress based on individual readiness. Pre-registration is required. For children ages 1 to 3.</div>
      </div>

      <div class="brand" style="top: 512px;">
        <span class="brand-mark"></span>
        <span class="brand-name">Harbor Grace<br>Health System</span>
      </div>

      <div class="photo photo--family" role="img" aria-label="Photo of two doctors standing beside a mother holding her baby"></div>
    </section>
  </div>
</body>
</html>
```